Veltarum

Standard Business Card design.
Sample two-sided design uploaded. White front, Black back.
Would like white shield to be on all black background side.
Willing to look at a couple creative designs, but nothing crazy.
Preference for a classic, confident, strong design.

```html
<!DOCTYPE html>
<html lang="en">
<head>
<meta charset="utf-8">
<title>Veltarum Business Card</title>
<link rel="stylesheet" href="https://fonts.googleapis.com/css2?family=Jost:wght@400;500;600&display=swap">
<style>
  :root {
    --stage: #5a5a5a;
    --ink: #111111;
    --paper: #f4f4f4;
    --muted: #6b6b6b;
    --rule: #9a9a9a;
  }
  * { margin: 0; padding: 0; box-sizing: border-box; }
  html, body { width: 1200px; height: 900px; overflow: hidden; }
  body {
    background: var(--stage);
    font-family: "Jost", sans-serif;
    position: relative;
  }
  .card {
    position: absolute;
    left: 250px;
    width: 700px;
    height: 400px;
    overflow: hidden;
  }
  .card--back { top: 40px; background: var(--ink); }
  .card--front { top: 470px; background: var(--paper); color: var(--ink); }

  .brand {
    display: flex;
    align-items: center;
    gap: 14px;
    font-weight: 600;
    letter-spacing: 0.12em;
    text-transform: uppercase;
  }
  .brand__dot { width: 14px; height: 14px; border-radius: 50%; background: currentColor; }

  .card--back .brand {
    position: absolute;
    left: 330px;
    top: 170px;
    color: #ffffff;
    font-size: 44px;
  }

  .card--front .brand {
    position: absolute;
    left: 40px;
    top: 48px;
    font-size: 34px;
  }
  .front__rule {
    position: absolute;
    left: 0;
    top: 170px;
    width: 420px;
    height: 1px;
    background: var(--rule);
  }
  .person { position: absolute; left: 140px; top: 220px; }
  .person__name { font-size: 22px; font-weight: 600; letter-spacing: 0.04em; }
  .person__role { font-size: 17px; color: var(--muted); margin-top: 2px; }

  .contact__rule {
    position: absolute;
    left: 0;
    top: 300px;
    width: 260px;
    height: 1px;
    background: var(--rule);
  }
  .contact {
    position: absolute;
    left: 140px;
    top: 280px;
    list-style: none;
    font-size: 17px;
    line-height: 30px;
  }
  .contact li { display: flex; align-items: center; gap: 10px; }
  .contact svg { width: 16px; height: 16px; fill: none; stroke: var(--ink); stroke-width: 1.6; }
  .address {
    position: absolute;
    left: 360px;
    top: 262px;
    padding-left: 16px;
    border-left: 1px solid var(--ink);
    font-size: 19px;
    line-height: 26px;
  }
</style>
</head>
<body>
  <section class="card card--back">
    <div class="brand"><span class="brand__dot"></span>Veltarum</div>
  </section>

  <section class="card card--front">
    <div class="brand"><span class="brand__dot"></span>Veltarum</div>
    <div class="front__rule"></div>

    <div class="person">
      <p class="person__name">DANIEL REYES</p>
      <p class="person__role">Director</p>
    </div>

    <ul class="contact">
      <li>
        <svg viewBox="0 0 16 16"><path d="M4 1.5l2.5 3-1.5 1.5a8 8 0 0 0 5 5l1.5-1.5 3 2.5-1.5 2.5C7 14 2 9 1.5 3z"/></svg>
        300-410-7200
      </li>
      <li>
        <svg viewBox="0 0 16 16"><rect x="1.5" y="3.5" width="13" height="9"/><path d="M1.5 3.5l6.5 5 6.5-5"/></svg>
        info@veltarum.com
      </li>
      <li>
        <svg viewBox="0 0 16 16"><circle cx="8" cy="8" r="6.5"/><ellipse cx="8" cy="8" rx="3" ry="6.5"/><path d="M1.5 8h13"/></svg>
        www.veltarum.com
      </li>
    </ul>

    <div class="address">
      <p>00 dummy city</p>
      <p>place 0000</p>
    </div>
  </section>
</body>
</html>
```